Book Cover for Self Help Book Teens

I need a standard a5 size book cover (front and back) for my new self help book for teens. The book is called
WHEN DAYS DRAG
ideas and tactics for teens in tough times
break ups, school problems, procrastination, fights, sexuality, alcohol, bitchiness, eating problems, can’t sleep, no motivation, not allowed to do stuff, being on the outer..and 34 other common situations that every day Australian teens face
Brenna Faldow
psychologist for teens
I would like a very sparse,very modern cover, no photos - maybe just cartoon-y graphic of smiley face upside down - ie frowny face. Few colours in order to make it look bold. lots of space on the cover.
I will provide back cover text soon
Updates
I just want to say that I really appreciate all of your efforts, the designs were excellent. As a thankyou, I'm happy to email you a link to the e-version of this book if you are interested. Just email me at brennafaldow@quillmarsh.example and I will send it through as soon as it is completed.
Target Market(s)
teens....but parents will also be buying book
Industry/Entity Type
School
Look and feel

```html
<!DOCTYPE html>
<html lang="en">
<head>
<meta charset="utf-8">
<title>When Days Drag — Book Cover</title>
<link href="https://fonts.googleapis.com/css2?family=Arimo:ital,wght@0,400;1,400;1,700&family=Roboto:ital,wght@0,100;0,300;1,300&family=Permanent+Marker&family=Shadows+Into+Light&display=swap" rel="stylesheet">
<style>
  :root {
    --band: #000000;
    --paper: #f3f3f2;
    --ink: #1e1e1e;
    --ink-soft: #2e2e2e;
    --muted: #8a8a8a;
    --title-red: #d8234a;
    --title-purple: #5e2a8c;
    --title-lilac: rgba(150, 110, 200, 0.45);
    --title-pink: rgba(230, 120, 150, 0.35);
    --wash-pink: rgba(225, 140, 160, 0.10);
    --wash-lilac: rgba(160, 120, 200, 0.10);
    --divider: #2a2a2a;
  }
  * { margin: 0; padding: 0; box-sizing: border-box; }
  html, body { width: 1200px; height: 900px; overflow: hidden; background: var(--band); }
  .canvas {
    position: relative; width: 1200px; height: 900px;
    background: var(--band);
    font-family: "Arimo", Arial, sans-serif;
    color: var(--ink);
  }
  .spread {
    position: absolute; left: 0; top: 25px; width: 1200px; height: 850px;
    background: var(--paper);
  }
  .spine-line {
    position: absolute; left: 600px; top: 0; width: 1px; height: 850px;
    background: var(--divider);
  }

  /* Back cover */
  .back { position: absolute; left: 0; top: 0; width: 600px; height: 850px; }
  .back-art {
    position: absolute; left: 0; top: 170px; width: 520px; height: 660px;
    background: radial-gradient(ellipse 45% 55% at 30% 45%, var(--wash-pink), transparent 70%),
                radial-gradient(ellipse 40% 45% at 75% 30%, var(--wash-lilac), transparent 70%);
  }
  .back-intro {
    position: absolute; left: 42px; top: 68px; width: 516px;
    font-family: "Roboto", Arial, sans-serif;
    font-size: 19px; font-style: italic; font-weight: 300; line-height: 24.5px;
    text-align: justify; hyphens: auto; -webkit-hyphens: auto; color: var(--ink);
  }
  .topic {
    position: absolute; left: 42px; width: 516px;
    font-size: 13.6px; line-height: 17px; text-align: justify; color: var(--ink-soft);
  }
  .topic-label { font-weight: 700; font-style: italic; color: var(--ink); }
  .topic-friendships { top: 203px; }
  .topic-relationships { top: 289px; }
  .topic-parents { top: 391px; }
  .topic-school { top: 493px; }
  .topic-health { top: 579px; }
  .back-closing {
    position: absolute; left: 42px; top: 705px; width: 516px;
    font-family: "Roboto", Arial, sans-serif;
    font-size: 19px; font-style: italic; font-weight: 300; line-height: 24px;
  }
  .back-web {
    position: absolute; left: 0; top: 776px; width: 600px; text-align: center;
    font-family: "Roboto", Arial, sans-serif;
    font-size: 21px; font-style: italic; font-weight: 300; color: var(--muted);
  }

  /* Front cover */
  .front { position: absolute; left: 600px; top: 0; width: 600px; height: 850px; }
  .book-title {
    position: absolute; left: 30px; top: 150px; width: 560px;
    font-family: "Permanent Marker", cursive;
    font-weight: 400; line-height: 1;
  }
  .title-top {
    display: block; font-size: 88px; color: var(--title-red);
    text-shadow: 5px 4px 0 var(--title-pink);
    transform: rotate(-4deg); margin-left: 12px;
  }
  .title-bottom {
    display: block; font-size: 150px; color: var(--title-purple);
    text-shadow: 10px 8px 0 var(--title-lilac);
    margin-top: 10px; margin-left: 110px; letter-spacing: 2px;
  }
  .tagline {
    position: absolute; left: 283px; top: 512px; width: 280px;
    font-family: "Shadows Into Light", cursive;
    font-size: 21px; line-height: 24px; color: var(--ink);
    transform: rotate(-2deg);
  }
  .author-swoosh {
    position: absolute; left: 110px; top: 720px; width: 340px; height: 90px;
    background: radial-gradient(ellipse at center, rgba(160, 120, 200, 0.22), transparent 70%);
    transform: rotate(-5deg);
  }
  .author-name {
    position: absolute; left: 0; top: 705px; width: 600px; text-align: center;
    font-family: "Roboto", Arial, sans-serif;
    font-size: 46px; font-weight: 100; letter-spacing: -0.5px; line-height: 54px;
    color: var(--ink);
  }
  .author-role {
    position: absolute; left: 0; top: 759px; width: 600px; text-align: center;
    font-family: "Roboto", Arial, sans-serif;
    font-size: 20px; font-weight: 300; color: var(--ink);
  }
</style>
</head>
<body>
<main class="canvas">
  <div class="spread">
    <section class="back">
      <div class="back-art" role="img" aria-label="Faint hand-drawn stick figures in pink and lilac"></div>
      <p class="back-intro">Brenna Faldow is a clinical psychologist and has worked with hundreds of teens in the last 15 years. In this book she addresses 30 of the most frequent stressful and scary issues that teens face, and gives extremely practical what to do (and what NOT to do) advice in each situation. Topics include:</p>
      <p class="topic topic-friendships"><span class="topic-label">FRIENDSHIPS:</span>&nbsp; My other friends seem to like each other more than me…..My friends are bitching about a friend of mine…..People at my school are horrible to me…..I have hardly any friends…..My friend is really depressed and I don’t know what to do…..</p>
      <p class="topic topic-relationships"><span class="topic-label">RELATIONSHIPS:</span>&nbsp; I hate being single…..I think I’m gay/bi :&nbsp; How do I know for sure?.....My boyfriend/girlfriend broke up with me and I’m devastated…..I’ve sent my boyfriend naked pics of myself, is this really that bad?.....I cheated on my boyfriend/girlfriend and I feel guilty…..My boyfriend/girlfriend cheated on me…..I don’t feel good about having sex with this person…</p>
      <p class="topic topic-parents"><span class="topic-label">PARENTS:</span>&nbsp; My parents are ALWAYS nagging me to do stuff I don’t want to do…..My parents don’t let me do anything or if I’m allowed it has to be this big drama……I’ve had a massive fight with my parents (again) and feel totally furious with them……My parents and I just don’t have anything in common, we hardly ever talk……</p>
      <p class="topic topic-school"><span class="topic-label">SCHOOL:</span>&nbsp; I’ve really got to do homework but I have zero motivation…..I really can’t stand my school and want to move but my parents won’t let me…..I’m seriously behind, have way too much to do and I’m not going to get it all done…..This assignment/work at school/course is just too complicated, I’m not smart enough…..</p>
      <p class="topic topic-health"><span class="topic-label">HEALTH AND SELF:</span>&nbsp; My sleep is terrible …..I drank way too much last night and probably last weekend as well…..I need to stop smoking weed/taking pills ……I hate the way I look……I’m skipping meals- I feel guilty but I need to lose weight…..I cut myself and it makes me feel better……I think about awful things - I could never tell anyone about them……Sometimes I feel so angry, I feel out of control……I just feel awful and down, and I don’t even know why</p>
      <p class="back-closing">This is the perfect reference book for teens in tough times, and for teens who might face tough times in the future.</p>
      <p class="back-web">www.quillmarshminds.example</p>
    </section>
    <div class="spine-line"></div>
    <section class="front">
      <h1 class="book-title">
        <span class="title-top">WHEN DAYS</span>
        <span class="title-bottom">DRAG</span>
      </h1>
      <p class="tagline">ideas and tactics for<br>&nbsp;&nbsp;&nbsp;&nbsp;&nbsp;&nbsp;teens in tough times</p>
      <div class="author-swoosh" role="img" aria-label="Soft lilac brush swoosh"></div>
      <h2 class="author-name">Brenna Faldow</h2>
      <p class="author-role">psychologist for teens</p>
    </section>
  </div>
</main>
</body>
</html>
```